Design a poster for Ellery's Dash 2023. A charity event supporting paediatric brain cancer.

We need a new poster for our event in 2023. The successful applicant will have opportunity for ongoing work with our foundation as we need a number of other deliverables once the design is finalised. We have a strong, fun and youthful brand.
Please see attached PDF showing the last 10 years of designs.
Please see attached moodboards outlining concepts for our 2023 theme. The last image of skateboarder concept is "Dusky Glow" - A retro miami vibe Juxtaposed with photo of someone from one of our previous events. Potentially posters could have multiple variants building on lots of different photos.
I have attached our brand guidelines as well as lock ups for our Ellery's Dash logos.
Whatever is created needs to be transferrable on to a number of different mediums, most importantly T-shirts, Web Banners, Billboards, Pavement Stickers, Social posts.
Our sponsor logos will remain the same.
Please only send complete designs - aligned with one of the 4 concepts provided and include all copy as per attached and include sponsors logos. Please ensure the body fonts are Brandon Grotesque and CCMatinee Idol.
Updates
Hi All, Thank you so much for all the submissions. Unfortunately after our CEO and team have reviewed the designs they are looking to go in quite a different direction than the original brief provided. I apologise for wasting your time. I have updated brief, and more specific moodboards, the last image concept is "Dusky Glow" - A retro miami vibe Juxtaposed with photo of someone from one of our previous events. Potentially posters could have multiple variants building on lots of different photos . If you would like to submit another design that would be great but if not we completely understand. Thank you again for your creative submissions.
Target Market(s)
18-35 year olds
Industry/Entity Type
Not for Profit - Fun Run Event and Party
Font styles to use
Other font styles liked:
- Fonts in Brand Guidelines - Brandon Grotesque and CCMatinee Idol
Requirements
Must have
- On Brand - colourful, focus on ALL SMILES NO MILES

```html
<!DOCTYPE html>
<html lang="en">
<head>
<meta charset="utf-8">
<title>Ellery's Dash 2023 — Fun Run and Party</title>
<link href="https://fonts.googleapis.com/css2?family=Anton&family=Archivo:wght@400;600;700;800;900&family=Dancing+Script:wght@700&display=swap" rel="stylesheet">
<style>
  :root{
    --page:#ffffff;
    --plum-dark:#66164f;
    --plum:#a34c8c;
    --orchid:#b05ea2;
    --berry:#b02a52;
    --magenta:#b3367e;
    --violet:#713d97;
    --navy:#1d2547;
    --yellow:#f5c400;
    --lemon:#fff200;
    --white:#ffffff;
    --ink:#1a1a1a;
  }
  *{box-sizing:border-box;margin:0;padding:0}
  html,body{width:1078px;height:1200px;overflow:hidden;background:var(--page)}
  .canvas{position:relative;width:1078px;height:1200px;background:var(--page);border:1px solid #d8d8d8}
  .poster{position:absolute;left:242px;top:180px;width:594px;height:840px;overflow:hidden;background:var(--plum);font-family:"Archivo",Arial,sans-serif;color:var(--white)}
  .poster__art{position:absolute;left:0;top:0;width:594px;height:708px;
    background:
      radial-gradient(ellipse 180px 260px at 40% 45%, var(--plum-dark) 0%, transparent 70%),
      radial-gradient(ellipse 160px 200px at 10% 40%, var(--berry) 0%, transparent 70%),
      radial-gradient(ellipse 140px 240px at 90% 60%, var(--magenta) 0%, transparent 70%),
      radial-gradient(ellipse 120px 160px at 15% 85%, var(--plum-dark) 0%, transparent 70%),
      radial-gradient(ellipse 100px 120px at 5% 62%, var(--violet) 0%, transparent 70%),
      linear-gradient(160deg, var(--plum) 0%, var(--orchid) 50%, var(--plum) 100%);}
  .kicker{position:absolute;left:0;width:100%;text-align:center;font-weight:700;font-size:15px;letter-spacing:.2px}
  .kicker--cause{top:54px;color:var(--white)}
  .kicker--cause::before,.kicker--cause::after{content:"";display:inline-block;width:14px;height:9px;background:var(--white);vertical-align:1px;margin:0 4px}
  .kicker--cause::before{clip-path:polygon(0 0,100% 0,100% 100%,0 100%,35% 50%)}
  .kicker--cause::after{clip-path:polygon(0 0,100% 0,65% 50%,100% 100%,0 100%)}
  .kicker--mission{top:79px;color:var(--lemon)}
  .event-title{position:absolute;left:0;top:128px;width:100%;text-align:center;font-weight:900;color:var(--white)}
  .event-title__name{display:block;font-size:64px;line-height:74px;letter-spacing:1px}
  .event-title__name + .event-title__name{font-size:84px;line-height:88px;letter-spacing:6px}
  .event-title__when{display:block;margin-top:6px;font-weight:700;font-size:22px;line-height:26px;letter-spacing:4px}
  .event-box{position:absolute;left:113px;top:352px;width:368px;height:133px;text-align:center}
  .event-box::before,.event-box::after{content:"";position:absolute;top:0;width:34px;height:100%;border:3px solid #111}
  .event-box::before{left:0;border-right:none}
  .event-box::after{right:0;border-left:none}
  .event-box__title{margin-top:10px;font-weight:400;font-size:35px;line-height:36px;color:var(--yellow);letter-spacing:1px}
  .event-box__title em{font-family:"Dancing Script",cursive;font-style:normal;font-size:36px;letter-spacing:0;margin-right:6px}
  .event-box__date{margin-top:6px;font-size:26px;line-height:30px}
  .event-box__date sup{font-size:12px;vertical-align:12px}
  .tagline{position:absolute;left:0;top:506px;width:100%;text-align:center;font-family:"Anton",Impact,sans-serif;font-weight:400;font-size:35px;line-height:46px;text-shadow:2px 2px 0 var(--navy);letter-spacing:-.5px}
  .cta{position:absolute;left:62px;top:626px;width:316px;text-align:center;font-weight:700;font-size:16px;line-height:21px;letter-spacing:.3px}
  .cta__url{display:block;margin-top:6px;font-weight:800;font-size:22px;color:var(--lemon);letter-spacing:.2px;text-shadow:1px 1px 0 var(--navy)}
  .foundation{position:absolute;left:448px;top:609px;width:84px;height:84px;border-radius:50%;background:var(--navy);border:3px solid var(--white);display:flex;align-items:center;justify-content:center;text-align:center;font-weight:700;font-size:11px;line-height:13px;color:var(--white)}
  .sponsors{position:absolute;left:0;top:708px;width:594px;height:101px;background:var(--white);color:var(--ink)}
  .sponsors__label{position:absolute;top:13px;left:0;width:100%;text-align:center;font-size:12px}
  .sponsors__row{position:absolute;top:38px;left:48px;right:48px;height:44px;display:flex;justify-content:space-between;align-items:center}
  .sponsor{font-weight:700;font-size:14px;color:var(--navy);display:flex;align-items:center;gap:5px;white-space:nowrap}
  .sponsor__dot{width:10px;height:10px;border-radius:50%;background:var(--berry)}
  .poster__footer{position:absolute;left:0;top:809px;width:594px;height:31px;background:linear-gradient(90deg,var(--violet) 0%,var(--berry) 25%,var(--berry) 100%)}
</style>
</head>
<body>
<div class="canvas">
  <article class="poster">
    <div class="poster__art" role="img" aria-label="Flat illustration of runners in purple, magenta and crimson tones"></div>

    <p class="kicker kicker--cause">SUPPORTING MIND FORWARD</p>
    <p class="kicker kicker--mission">TO BEAT THE #1 CANCER KILLER OF YOUNG PEOPLE</p>

    <h1 class="event-title">
      <span class="event-title__name">ELLERY'S</span>
      <span class="event-title__name">DASH</span>
      <span class="event-title__when">SEPT 2023</span>
    </h1>

    <section class="event-box">
      <h2 class="event-box__title">FUN RUN<br><em>and</em>PARTY</h2>
      <p class="event-box__date">SUNDAY 10<sup>th</sup> SEPTEMBER</p>
    </section>

    <p class="tagline">A FUN RUN THAT ISN'T ABOUT<br>Running or Winning</p>

    <p class="cta">REGISTER OR SUPPORT<br>A PARTICIPANT AT<span class="cta__url">WWW.ELLERYSDASH.ORG</span></p>

    <div class="foundation">Ellery Dash<br>Foundation</div>

    <footer class="sponsors">
      <p class="sponsors__label">Supported By :</p>
      <div class="sponsors__row">
        <span class="sponsor">Grocera</span>
        <span class="sponsor">Cloudtide</span>
        <span class="sponsor">Signalboard</span>
        <span class="sponsor">Maple Homes</span>
        <span class="sponsor"><i class="sponsor__dot"></i>Kazemi Motors</span>
      </div>
    </footer>
    <div class="poster__footer" role="img" aria-label="Strip of the runners illustration in violet and crimson"></div>
  </article>
</div>
</body>
</html>
```